PREMIUM AGENCY High End Business Card - A+++ Designers Wanted

** DO NOT ATTEMPT TO CONTACT ME THROUGH SEARCHING ON ZINTREL OR EMAILING ME THROUGH MY WEBSITE **

I need a fresh, contemporary business card designed using the logo attached (BRONSALK)

I have attached the font for BRONSALK

It must have a premium look and feel. The business card size must be STANDARD size.

You can submit either/both VERTICAL or HORIZONTAL designs.

FRONT: It must have the following sample information on

Paul Ardley
Director Operations
Mobile +61 452 118 906
Email paulardley@bronsalk.com
www.bronsalk.com

The REAR of the business card must have the words

CREATE INSPIRE TOMORROW

as part of the design, in the same font (NEXA) attached.

The words do not need to be in capitals, or on the same line, please design this as you see it best working.

ADDITIONAL INFORMATION
======================

The BRONSALK logo must be on the front of the card

I want Ultraviolet printing on the final design, to enhance either the NAME of the person OR the BRONSALK logo OR the words on the back of the card.

Target Market(s)

Agency, Advertising Agency, Creative, Designers

Industry/Entity Type

Media

Contact Information for Business Card

Design Agency, Contemporary, Premium look and feel, High Quality

Font styles to use
Serif
Sans Serif
Other font styles liked:
• ATTACHED TO PROJECT

Requirements
Must have
• BLACK & WHITE as the primary design, and if you feel there can be a highlighted colour, then this can be used.
• The Logo ICON attached is blue, this colour must not be changed.
• I have attached the partner brand BRONSALK MEDIA incase you need to manipulate the original files.
• ** DO NOT ATTEMPT TO CONTACT ME THROUGH SEARCHING ON ZINTREL OR EMAILING ME THROUGH MY WEBSITE **
Nice to have
• Must be Premium. I have attached some sample designs, that I like that would be a good inspiration for where this can be taken.
• My favourite design is is the KESTRAVUE2-BUSINESSCARD-TEMPLATE
Should not have
• No funny or silly standard / off the shelf designs

```html
<!DOCTYPE html>
<html lang="en">
<head>
<meta charset="utf-8">
<title>Bronsalk Media Business Card</title>
<link rel="stylesheet" href="https://fonts.googleapis.com/css2?family=Montserrat:wght@400;500;600&display=swap">
<style>
  :root {
    --bg: #f1f1f1;
    --ink: #2b2b2b;
    --card: #000000;
    --brand-blue: #239fd9;
    --logo-on-black: #262626;
    --name-white: #f4f4f4;
    --contact-grey: #3c3c3c;
    --rule: #2e2e2e;
  }
  * { margin: 0; padding: 0; box-sizing: border-box; }
  html, body { width: 1200px; height: 1200px; overflow: hidden; }
  body {
    background: var(--bg);
    font-family: "Montserrat", Arial, sans-serif;
    position: relative;
  }
  .brand-lockup {
    position: absolute;
    top: 68px;
    right: 80px;
    display: flex;
    align-items: center;
    gap: 16px;
  }
  .brand-dot {
    width: 30px; height: 30px;
    border-radius: 50%;
    background: var(--brand-blue);
  }
  .brand-name {
    font-size: 40px;
    font-weight: 600;
    letter-spacing: 3px;
    color: var(--ink);
  }
  .card {
    position: absolute;
    width: 520px;
    height: 297px;
    background: var(--card);
    box-shadow: 0 18px 30px rgba(0,0,0,0.22);
    overflow: hidden;
  }
  .card-rear { left: 80px; top: 250px; }
  .card-front { left: 600px; top: 620px; }

  .rear-lockup {
    position: absolute;
    inset: 0;
    display: flex;
    align-items: center;
    justify-content: center;
    gap: 14px;
  }
  .rear-dot {
    width: 20px; height: 20px;
    border-radius: 50%;
    background: var(--brand-blue);
  }
  .rear-name {
    font-size: 28px;
    font-weight: 600;
    letter-spacing: 3px;
    color: var(--logo-on-black);
  }

  .holder {
    position: absolute;
    left: 44px;
    bottom: 70px;
  }
  .holder-name {
    font-size: 28px;
    font-weight: 600;
    letter-spacing: 1px;
    color: var(--name-white);
    text-transform: uppercase;
  }
  .holder-role {
    margin-top: 4px;
    font-size: 11px;
    font-weight: 400;
    letter-spacing: 1.5px;
    color: var(--brand-blue);
    text-transform: uppercase;
  }
  .divider {
    position: absolute;
    left: 262px;
    top: 70px;
    width: 1px;
    height: 130px;
    background: var(--rule);
  }
  .contact-list {
    position: absolute;
    left: 284px;
    top: 92px;
    list-style: none;
  }
  .contact-item {
    display: flex;
    align-items: center;
    gap: 12px;
    height: 26px;
    font-size: 11px;
    color: var(--contact-grey);
  }
  .contact-icon { width: 14px; height: 14px; flex: none; }
</style>
</head>
<body>
  <header class="brand-lockup">
    <span class="brand-dot"></span>
    <span class="brand-name">BRONSALK MEDIA</span>
  </header>

  <section class="card card-rear" aria-label="Card rear with logo">
    <div class="rear-lockup">
      <span class="rear-dot"></span>
      <span class="rear-name">BRONSALK MEDIA</span>
    </div>
  </section>

  <section class="card card-front" aria-label="Card front with contact details">
    <div class="holder">
      <p class="holder-name">Paul Ardley</p>
      <p class="holder-role">Director Operations</p>
    </div>
    <div class="divider"></div>
    <ul class="contact-list">
      <li class="contact-item">
        <svg class="contact-icon" viewBox="0 0 14 14" fill="none" stroke="var(--brand-blue)" stroke-width="1.4">
          <rect x="4" y="1" width="6" height="12" rx="1.2"/>
          <line x1="6" y1="11" x2="8" y2="11"/>
        </svg>
        <span>+61 452 118 906</span>
      </li>
      <li class="contact-item">
        <svg class="contact-icon" viewBox="0 0 14 14" fill="var(--brand-blue)">
          <rect x="1" y="3" width="12" height="8"/>
          <polyline points="1,3 7,8 13,3" fill="none" stroke="#000" stroke-width="1"/>
        </svg>
        <span>paulardley@bronsalk.com</span>
      </li>
      <li class="contact-item">
        <svg class="contact-icon" viewBox="0 0 14 14" fill="none" stroke="var(--brand-blue)" stroke-width="1.2">
          <circle cx="7" cy="7" r="5.5"/>
          <ellipse cx="7" cy="7" rx="2.5" ry="5.5"/>
          <line x1="1.5" y1="7" x2="12.5" y2="7"/>
        </svg>
        <span>www.bronsalk.com</span>
      </li>
    </ul>
  </section>
</body>
</html>
```